KRL Banner Logo with Rocky Mountain of CO as the background

I need a banner/logo for my KRL year. So have a banner design that is like an intentional path or inspiring.

• KRL Silver Ridge CO mountain as background and they may add similar images that I sent you
• Wording: Intentional Path
Learning year 2025-2026
• Add the KRL logo (the white and blue image – you will see these online)

UPDATE: Attached are example images on how we envision the banner. Please do not use the attached example sample images. Kindly look for similar looking images that are FREE TO USE Commercially.

CEO, top executives

0054AA
0677BA
7BADD7
CADEEF
E8F1F8

• • KRL Silver Ridge CO mountain as background and they may add similar images that I sent you • Wording: Intentional Path Learning year 2025-2026 • Add the KRL logo (the white and blue image – you will see these online)
• It has nice to have the inspirational images attached but you can have your own design. This is only for sample.

```html
<!DOCTYPE html>
<html lang="en">
<head>
<meta charset="UTF-8">
<title>KRL Silver Ridge – Intentional Path Learning Year 2025-2026</title>
<link rel="stylesheet" href="https://fonts.googleapis.com/css2?family=Montserrat:ital,wght@0,400;1,800;1,900&display=swap">
<style>
  :root {
    --brand-navy: #054a94;
    --brand-deep: #0054aa;
    --brand-blue: #0677ba;
    --brand-sky: #7badd7;
    --brand-mist: #cadeef;
    --brand-ice: #e8f1f8;
    --sun-gold: #f4c45a;
    --haze: #b9c2c8;
    --ridge-grey: #6b6a70;
    --ridge-dark: #3f4048;
    --ink-white: #ffffff;
    --mark-grey: #2f2f2f;
  }
  html, body {
    margin: 0;
    padding: 0;
    width: 1200px;
    height: 216px;
    overflow: hidden;
  }
  .banner {
    position: relative;
    width: 1200px;
    height: 216px;
    overflow: hidden;
    background: var(--brand-navy);
    font-family: "Montserrat", sans-serif;
  }
  .banner__facets {
    position: absolute;
    left: 0; top: 0;
    width: 600px; height: 216px;
    background:
      radial-gradient(ellipse 260px 170px at 90px 40px, rgba(6,119,186,0.85) 0%, rgba(6,119,186,0.35) 55%, rgba(6,119,186,0) 100%),
      radial-gradient(ellipse 200px 120px at 120px 150px, rgba(6,119,186,0.5) 0%, rgba(6,119,186,0) 100%);
  }
  .banner__scene {
    position: absolute;
    left: 560px; top: 0;
    width: 640px; height: 216px;
    background:
      linear-gradient(90deg, var(--brand-navy) 0%, rgba(5,74,148,0.7) 14%, rgba(5,74,148,0.25) 30%, rgba(5,74,148,0) 45%),
      linear-gradient(90deg, rgba(0,0,0,0) 60%, rgba(150,120,100,0.55) 72%, rgba(130,108,92,0.7) 100%),
      radial-gradient(ellipse 150px 45px at 350px 128px, rgba(255,214,110,0.95) 0%, rgba(244,196,90,0.55) 45%, rgba(244,196,90,0) 100%),
      linear-gradient(180deg, #7d9fc4 0%, #b8c4cc 30%, #d9d2b4 52%, #a5a3a2 64%, var(--ridge-grey) 80%, var(--ridge-dark) 100%);
  }
  .brand {
    position: absolute;
    left: 34px;
    top: 139px;
    display: flex;
    align-items: center;
    gap: 16px;
  }
  .brand__square {
    width: 52px;
    height: 52px;
    background: var(--mark-grey);
  }
  .brand__name {
    color: var(--ink-white);
    font-weight: 400;
    font-size: 43px;
    line-height: 1;
  }
  .title {
    position: absolute;
    left: 486px;
    top: 30px;
    transform: translateX(-50%);
    margin: 0;
    text-align: center;
    color: var(--ink-white);
    font-style: italic;
    font-weight: 900;
    line-height: 1;
    white-space: nowrap;
  }
  .title__line { display: block; }
  .title__line--top {
    font-size: 52px;
    letter-spacing: 0.5px;
  }
  .title__line--main {
    font-size: 76px;
    margin-top: 0;
  }
  .title__line--year {
    font-size: 38px;
    font-weight: 800;
    margin-top: 6px;
  }
</style>
</head>
<body>
  <div class="banner">
    <div class="banner__facets" role="img" aria-label="Faceted light blue geometric pattern over the brand blue background"></div>
    <div class="banner__scene" role="img" aria-label="Photo of a stacked stone cairn on a mountain summit at sunset, with hazy ridges below a glowing cloudy sky"></div>

    <div class="brand">
      <span class="brand__square"></span>
      <span class="brand__name">KRL</span>
    </div>

    <h1 class="title">
      <span class="title__line title__line--top">INTENTIONAL PATH</span>
      <span class="title__line title__line--main">LEARNING</span>
      <span class="title__line title__line--year">YEAR 2025-2026</span>
    </h1>
  </div>
</body>
</html>
```